Tech comm company needs a homepage banner

We need a banner for our homepage that inspires people about the possibilities of their written content. Taking the document to the next level. We need some beautiful imagery that evokes the idea that information can be "components" or blocks and connect to other assets... chatbots, Voice, other systems, A design that inspires the mind to think about the possibilities of information. Attached are some images. We have a corporate account w Brisvale images, so please search that site.

1 page

```html
<!DOCTYPE html>
<html lang="en">
<head>
<meta charset="UTF-8">
<title>Homepage Banner</title>
<link rel="stylesheet" href="https://fonts.googleapis.com/css2?family=Montserrat:wght@400;600;700&display=swap">
<style>
  :root {
    --bg-deep: #3e2b64;
    --bg-mid: #3a3d75;
    --bg-teal: #0fb6af;
    --white: #ffffff;
    --text-soft: #e4dcef;
    --accent: #3cb6e8;
    --navy: #1f1a5e;
    --illus-purple: #7a4fb8;
    --illus-teal: #2fc7c0;
  }
  * { margin: 0; padding: 0; box-sizing: border-box; }
  html, body { width: 1200px; height: 531px; overflow: hidden; }
  body { font-family: "Montserrat", Arial, sans-serif; }

  .banner {
    position: relative;
    width: 1200px;
    height: 531px;
    overflow: hidden;
    background:
      radial-gradient(ellipse 520px 420px at 1230px -40px, var(--bg-teal) 0%, rgba(15,182,175,0.55) 35%, rgba(15,182,175,0) 75%),
      linear-gradient(100deg, var(--bg-deep) 0%, var(--bg-deep) 48%, var(--bg-mid) 72%, #2f6d8c 100%);
  }

  .circuit-decor {
    position: absolute;
    left: 0;
    top: 0;
    width: 450px;
    height: 330px;
    background:
      radial-gradient(ellipse 260px 150px at 170px 20px, rgba(60,200,200,0.28), rgba(60,200,200,0) 70%),
      radial-gradient(ellipse 120px 200px at 20px 140px, rgba(60,200,200,0.18), rgba(60,200,200,0) 70%);
  }

  .tech-illustration {
    position: absolute;
    left: 596px;
    top: 76px;
    width: 500px;
    height: 436px;
  }

  .hero-copy {
    position: absolute;
    left: 134px;
    top: 151px;
    width: 370px;
  }

  .hero-title {
    position: relative;
    padding-left: 23px;
    color: var(--white);
    font-weight: 700;
    font-size: 33px;
    line-height: 42px;
    letter-spacing: -0.3px;
  }
  .hero-title::before {
    content: "";
    position: absolute;
    left: 3px;
    top: 5px;
    width: 5px;
    height: 36px;
    background: var(--accent);
  }

  .hero-text {
    margin-top: 18px;
    color: var(--text-soft);
    font-size: 11.6px;
    line-height: 19px;
    font-weight: 400;
  }

  .hero-actions {
    display: flex;
    gap: 9px;
    margin-top: 21px;
    margin-left: 2px;
  }
  .btn {
    display: flex;
    align-items: center;
    justify-content: center;
    width: 126px;
    height: 36px;
    border-radius: 2px;
    font-size: 11.5px;
    font-weight: 600;
    text-decoration: none;
  }
  .btn-primary {
    background: var(--white);
    color: var(--navy);
    box-shadow: 0 3px 10px rgba(0,0,0,0.25);
  }
  .btn-outline {
    border: 1.5px solid var(--accent);
    color: var(--accent);
  }
</style>
</head>
<body>
  <section class="banner">
    <div class="circuit-decor" role="img" aria-label="Decorative circuit lines and glowing particles"></div>

    <div class="hero-copy">
      <h1 class="hero-title">Lorem ipsum dolor sit amet, adipise</h1>
      <p class="hero-text">Lorem ipsum dolor sit amet, consectetur adipiscing elit. Cras sit amet mi convallis, sodales lectus vel, molestie leo. Cras porttitor efficitur sapien ut ullamcorper.</p>
      <div class="hero-actions">
        <a class="btn btn-primary" href="#">Learn More</a>
        <a class="btn btn-outline" href="#">Get in Touch</a>
      </div>
    </div>

    <svg class="tech-illustration" viewBox="0 0 500 436" role="img" aria-label="Isometric illustration of a laptop, desktop monitor, keyboard and phone linked to floating content blocks, cloud and wifi symbols on a glowing grid">
      <defs>
        <linearGradient id="illus-fill" x1="0" y1="1" x2="1" y2="0">
          <stop offset="0" stop-color="#7a4fb8" stop-opacity="0.75"/>
          <stop offset="0.5" stop-color="#5a5fb0" stop-opacity="0.7"/>
          <stop offset="1" stop-color="#2fc7c0" stop-opacity="0.8"/>
        </linearGradient>
      </defs>
      <polygon points="250,0 500,124 500,312 250,436 0,312 0,124" fill="url(#illus-fill)"/>
    </svg>
  </section>
</body>
</html>
```